Vro Klinieken website for a maxillofacial surgery clinic

It's a website for a clinic for maxillofacial surgery in WordPress . The website doesn't need to be complicated but has to look professional. It needs to be in Dutch so i can give the texts. Similar websites are www.tandartsenpraktijkvelmor.nl or www.tbospecialisten.nl. Pages would be sort of similar to https://hetcentrumvoorgezichtszorg.nl/ or https://wolderveenclinics.nl/. Those lasts are maxillofacial surgery clinic websites, but there are little more extensive.
I uploaded the logo. If this is not the proper quality i can upload the eps. Logo was made through printhive.

Target Market(s)

Patients who can find me and see information about the clinic

Industry/Entity Type

Healthcare

Coding

Coded - Design and coding required

Number of Pages Required

5+ page

Font styles to use
Other font styles liked:
• Something standard professional

Colors
0054AA
0677BA
7BADD7
CADEEF
E8F1F8

Requirements
Nice to have
• Something in line with the logo. I prefer a little dark like the darker logos but I'm not sure if that's professional. Logos zbpor and gvls are instances i'm registered to so they will have to be on the website too but small somewhere.

```html
<!DOCTYPE html>
<html lang="nl">
<head>
<meta charset="utf-8">
<title>Vro Klinieken Zoetermeer</title>
<link rel="stylesheet" href="https://fonts.googleapis.com/css2?family=Roboto:wght@400;500;700;900&family=Montserrat:wght@400;500&display=swap">
<style>
:root{
  --blue:#29a3df;
  --blue-dark:#1b8fcc;
  --ink:#222;
  --text:#444;
  --muted:#777;
  --dark:#1c1c1e;
  --light:#f2f3f5;
  --white:#fff;
}
*{margin:0;padding:0;box-sizing:border-box}
html,body{width:1200px;height:3694px;overflow:hidden}
body{position:relative;font-family:"Roboto",Arial,sans-serif;color:var(--ink);background:var(--white)}
.abs{position:absolute}
.btn{position:absolute;display:flex;align-items:center;justify-content:center;background:var(--blue);color:var(--white);border-radius:26px;font-weight:700;font-size:15px;letter-spacing:.2px}

/* header */
.site-header{position:absolute;left:0;top:0;width:1200px;height:125px;background:var(--white)}
.brand{position:absolute;left:118px;top:44px;display:flex;align-items:center;gap:8px;font-size:24px;font-weight:700;color:var(--blue)}
.brand-dot{width:16px;height:16px;border-radius:50%;background:var(--blue)}
.nav{position:absolute;top:54px;font-size:15px;color:#333}

/* hero */
.hero{position:absolute;left:0;top:125px;width:1200px;height:642px;overflow:hidden}
.hero-photo{position:absolute;inset:0;background:linear-gradient(110deg,#4b5563 0%,#8a96a3 45%,#c9d3dc 75%,#9aa8b6 100%)}
.hero-shade{position:absolute;inset:0;background:linear-gradient(90deg,rgba(30,35,45,.55),rgba(30,35,45,.05) 60%)}
.hero-title{position:absolute;left:110px;top:180px;font-size:80px;line-height:92px;font-weight:700;color:var(--white)}

/* about */
.about-photo{position:absolute;left:112px;top:862px;width:452px;height:406px;border:5px solid var(--blue);border-radius:12px;background:linear-gradient(135deg,#eef2f5,#cfdbe4 60%,#9fc7de)}
.about-title{position:absolute;left:642px;top:878px;font-size:31px;font-weight:500}
.about-title span{color:var(--blue)}
.about-text{position:absolute;left:642px;top:944px;width:432px;font-size:15px;line-height:27.5px;color:var(--text)}

/* services */
.services{position:absolute;left:0;top:1354px;width:1200px;height:634px;background:linear-gradient(120deg,#2e3237,#4a5058 50%,#33373c)}
.services-title{position:absolute;top:96px;width:100%;text-align:center;font-size:30px;font-weight:500;color:var(--white)}
.service-card{position:absolute;top:223px;width:308px;height:311px;border:2px solid #e5e5e5;border-radius:22px;text-align:center;color:var(--white)}
.service-card.is-active{background:var(--blue);border-color:var(--blue)}
.service-icon{position:absolute;left:50%;top:-47px;width:120px;height:100px;margin-left:-60px;background:var(--blue);display:flex;align-items:center;justify-content:center}
.is-active .service-icon{background:var(--white);border-radius:4px}
.service-card h3{position:absolute;top:92px;width:100%;font-size:25px;font-weight:500}
.service-card p{position:absolute;top:146px;left:24px;right:24px;font-size:16px;line-height:26px}
.service-more{position:absolute;left:50%;bottom:18px;margin-left:-11px}

/* testimonials */
.section-title{position:absolute;width:100%;text-align:center;font-size:30px;font-weight:700;color:var(--ink)}
.quote{position:absolute;width:290px;text-align:center}
.quote p{margin-top:18px;font-size:14.5px;line-height:24px;color:var(--muted)}
.quote strong{display:block;margin-top:14px;font-size:14.5px;font-weight:500;color:var(--ink)}

/* blog */
.blog{position:absolute;left:0;top:2406px;width:1200px;height:900px;background:var(--light)}
.post{position:absolute;background:var(--white);box-shadow:0 2px 10px rgba(0,0,0,.06)}
.post-photo{position:absolute;background:linear-gradient(135deg,#dfe8ef,#9fc4dc 55%,#6f8ea8)}
.post-title{position:absolute;font-family:"Montserrat",sans-serif;font-size:19px;line-height:28px;color:var(--ink)}
.post-title.is-link{color:var(--blue)}
.post-date{position:absolute;font-family:"Montserrat",sans-serif;font-size:15px;color:#888;display:flex;align-items:center;gap:8px}
.post-more{position:absolute;font-size:14.5px;font-weight:700;color:var(--blue)}

/* footer */
.footer{position:absolute;left:0;top:3230px;width:1200px;height:464px}
.footer-body{position:absolute;left:0;top:60px;width:1200px;height:404px;background:var(--dark)}
.f-head{position:absolute;font-size:19px;font-weight:700;color:var(--white)}
.f-list{position:absolute;list-style:none;font-size:15px;color:#eee}
.f-list li{height:25.7px;display:flex;align-items:center;gap:12px}
.f-contact{position:absolute;font-size:15px;line-height:25px;color:#eee}
.social{position:absolute;top:3550px;width:36px;height:36px;border-radius:50%;background:var(--white)}
.copyright{position:absolute;top:3646px;width:100%;text-align:center;font-size:15px;color:#eee}
</style>
</head>
<body>

<header class="site-header">
  <div class="brand"><span class="brand-dot"></span>Vro Klinieken</div>
  <span class="nav" style="left:357px">Thuis</span>
  <span class="nav" style="left:433px">Behandelingen</span>
  <span class="nav" style="left:573px">Over ons</span>
  <span class="nav" style="left:671px">Diensten</span>
  <span class="nav" style="left:770px">Bloggen</span>
  <span class="nav" style="left:864px">Contact</span>
  <span class="btn" style="left:972px;top:40px;width:116px;height:50px">LOG IN</span>
</header>

<section class="hero">
  <div class="hero-photo" role="img" aria-label="Tandarts en assistente behandelen een patiënt in de behandelstoel"></div>
  <div class="hero-shade"></div>
  <h1 class="hero-title">Vro Klinieken<br>Zoetermeer</h1>
  <span class="btn" style="left:112px;top:390px;width:142px;height:50px">GET STARTED</span>
  <svg class="abs" style="left:0;bottom:0" width="1200" height="130" viewBox="0 0 1200 130">
    <path d="M0 70 C200 140 420 110 640 70 C860 30 1020 -10 1200 30 L1200 130 L0 130Z" fill="var(--blue)"/>
    <path d="M0 90 C200 150 420 125 640 88 C860 52 1020 15 1200 52 L1200 130 L0 130Z" fill="var(--white)"/>
  </svg>
</section>

<section class="about">
  <div class="about-photo" role="img" aria-label="Moderne behandelkamer met blauwe tandartsstoelen en medewerkers"></div>
  <h2 class="about-title">OVER <span>ONS</span></h2>
  <p class="about-text">Lorem ipsum dolor sit amet, consectetur adipiscing elit, sed do eiusmod tempor incididunt ut labore et dolore magna aliqua. Ut enim ad minim veniam, quis nostrud exercitation ullamco laboris nisi ut aliquip ex ea commodo consequat. Duis aute irure dolor in reprehenderit in voluptate velit esse cillum dolore eu fugiat nulla pariatur. Excepteur sint occaecat cupidatat non proident, sunt in culpa qui officia deserunt mollit anim id est laborum.</p>
  <span class="btn" style="left:642px;top:1192px;width:150px;height:50px">LEARN MORE</span>
</section>

<section class="services" role="img" aria-label="Gedimde achtergrond met behandeling in de tandartspraktijk">
  <h2 class="services-title">ONZE DIENSTEN</h2>

  <div class="service-card" style="left:110px">
    <div class="service-icon"><svg width="60" height="60" viewBox="0 0 60 60" fill="none" stroke="#fff" stroke-width="2"><circle cx="30" cy="30" r="22"/><path d="M18 26 Q30 16 42 26 Q30 46 18 26Z"/></svg></div>
    <h3>Lorem ipsum dolo</h3>
    <p>Lorem ipsum dolor sit amet, consectetur adipiscing elit, sed do eiusmod tempor incididunt ut labore et dolore magna aliqua.</p>
    <svg class="service-more" width="22" height="22" viewBox="0 0 22 22"><circle cx="11" cy="11" r="10" fill="var(--blue)"/><path d="M6.5 9 L11 13.5 L15.5 9" stroke="#fff" stroke-width="2.4" fill="none"/></svg>
  </div>

  <div class="service-card is-active" style="left:448px;width:304px">
    <div class="service-icon"><svg width="62" height="62" viewBox="0 0 62 62" fill="none" stroke="var(--blue)" stroke-width="2"><path d="M12 20 C12 8 26 8 31 14 C36 8 50 8 50 20 C50 32 46 36 44 54 L38 54 L35 38 L27 38 L24 54 L18 54 C16 36 12 32 12 20Z"/></svg></div>
    <h3>Lorem ipsum dolo</h3>
    <p>Lorem ipsum dolor sit amet, consectetur adipiscing elit, sed do eiusmod tempor incididunt ut labore et dolore magna aliqua.</p>
    <svg class="service-more" width="22" height="22" viewBox="0 0 22 22"><circle cx="11" cy="11" r="10" fill="#fff"/><path d="M6.5 9 L11 13.5 L15.5 9" stroke="var(--blue)" stroke-width="2.4" fill="none"/></svg>
  </div>

  <div class="service-card" style="left:782px">
    <div class="service-icon"><svg width="60" height="60" viewBox="0 0 60 60" fill="none" stroke="#fff" stroke-width="2"><path d="M12 48 L44 16 M20 52 L52 20 M40 12 L48 20"/></svg></div>
    <h3>Lorem ipsum dolo</h3>
    <p>Lorem ipsum dolor sit amet, consectetur adipiscing elit, sed do eiusmod tempor incididunt ut labore et dolore magna aliqua.</p>
    <svg class="service-more" width="22" height="22" viewBox="0 0 22 22"><circle cx="11" cy="11" r="10" fill="var(--blue)"/><path d="M6.5 9 L11 13.5 L15.5 9" stroke="#fff" stroke-width="2.4" fill="none"/></svg>
  </div>
</section>

<section class="testimonials">
  <h2 class="section-title" style="top:2064px">WAT ONZE KLANTEN ZEGGEN</h2>
  <svg class="abs" style="left:66px;top:2240px" width="18" height="32" viewBox="0 0 18 32"><path d="M16 2 L3 16 L16 30" stroke="var(--blue)" stroke-width="2" fill="none"/></svg>
  <svg class="abs" style="left:1116px;top:2240px" width="18" height="32" viewBox="0 0 18 32"><path d="M2 2 L15 16 L2 30" stroke="var(--blue)" stroke-width="2" fill="none"/></svg>

  <div class="quote" style="left:106px;top:2152px">
    <svg width="52" height="44" viewBox="0 0 52 44"><path d="M2 28 C2 12 10 4 22 2 L22 10 C14 12 12 18 12 22 L22 22 L22 42 L2 42Z M30 28 C30 12 38 4 50 2 L50 10 C42 12 40 18 40 22 L50 22 L50 42 L30 42Z" fill="var(--blue)"/></svg>
    <p>Loremipsumjidolorkgiusitamet, consectetur adipiscelit,seddoeiusmod temporincididunt ut labore et dolore magna aliqua.</p>
    <strong>- JAN SMIT</strong>
  </div>
  <div class="quote" style="left:454px;top:2152px">
    <svg width="52" height="44" viewBox="0 0 52 44"><path d="M2 28 C2 12 10 4 22 2 L22 10 C14 12 12 18 12 22 L22 22 L22 42 L2 42Z M30 28 C30 12 38 4 50 2 L50 10 C42 12 40 18 40 22 L50 22 L50 42 L30 42Z" fill="var(--blue)"/></svg>
    <p>Loremipsumjidolorgiusitamet, consectetur adipiscelit,seddoeiusmod temporincididunt ut labore et dolore magna aliqua.</p>
    <strong>- JAN SMIT</strong>
  </div>
  <div class="quote" style="left:802px;top:2152px">
    <svg width="52" height="44" viewBox="0 0 52 44"><path d="M2 28 C2 12 10 4 22 2 L22 10 C14 12 12 18 12 22 L22 22 L22 42 L2 42Z M30 28 C30 12 38 4 50 2 L50 10 C42 12 40 18 40 22 L50 22 L50 42 L30 42Z" fill="var(--blue)"/></svg>
    <p>Loremipsumjidolorgiusitamet, consectetur adipiscelit,seddoeiusmod temporincididunt ut labore et dolore magna aliqua.</p>
    <strong>- JAN SMIT</strong>
  </div>
</section>

<section class="blog">
  <h2 class="section-title" style="top:76px">NIEUWSTE BLOG</h2>

  <article class="post" style="left:112px;top:162px;width:488px;height:497px">
    <div class="post-photo" style="left:12px;top:13px;width:463px;height:318px" role="img" aria-label="Handen in handschoenen houden een gebitsmodel boven röntgenfoto's"></div>
    <h3 class="post-title" style="left:12px;top:352px">Sed ut perspiciatis unde omnis iste natus error</h3>
    <div class="post-date" style="left:12px;top:395px"><svg width="14" height="14" viewBox="0 0 14 14"><rect x="1" y="2" width="12" height="11" fill="#aaa"/></svg>December 28,2023</div>
    <span class="post-more" style="left:12px;top:451px">READ MORE →</span>
  </article>

  <article class="post" style="left:635px;top:162px;width:453px;height:240px">
    <div class="post-photo" style="left:10px;top:11px;width:190px;height:218px" role="img" aria-label="Patiënt in gesprek met een medewerker van de kliniek"></div>
    <h3 class="post-title is-link" style="left:230px;top:36px">Sed ut perspiciatis<br>unde omnis iste</h3>
    <div class="post-date" style="left:230px;top:110px"><svg width="14" height="14" viewBox="0 0 14 14"><rect x="1" y="2" width="12" height="11" fill="#aaa"/></svg>December 28,2023</div>
    <span class="post-more" style="left:230px;top:182px">READ MORE →</span>
  </article>

  <article class="post" style="left:635px;top:420px;width:453px;height:239px">
    <div class="post-photo" style="left:10px;top:11px;width:190px;height:218px;background:linear-gradient(135deg,#e9ecef,#c8ccd1 60%,#a9aeb5)" role="img" aria-label="Portret van een lachende oudere vrouw"></div>
    <h3 class="post-title" style="left:230px;top:36px">Sed ut perspiciatis<br>unde omnis iste</h3>
    <div class="post-date" style="left:230px;top:110px"><svg width="14" height="14" viewBox="0 0 14 14"><rect x="1" y="2" width="12" height="11" fill="#aaa"/></svg>December 28,2023</div>
    <span class="post-more" style="left:230px;top:172px">READ MORE →</span>
  </article>

  <span class="btn" style="left:525px;top:693px;width:150px;height:53px;font-size:14px">BEKIJK MEER</span>
</section>

<footer class="footer">
  <svg class="abs" style="left:0;top:0" width="1200" height="70" viewBox="0 0 1200 70">
    <path d="M0 40 C200 -10 420 5 640 40 C860 75 1040 60 1200 22 L1200 70 L0 70Z" fill="var(--blue)"/>
    <path d="M0 58 C200 15 420 30 640 58 C860 86 1040 80 1200 50 L1200 70 L0 70Z" fill="var(--dark)"/>
  </svg>
  <div class="footer-body"></div>
</footer>

<div class="brand" style="left:130px;top:3446px;color:var(--blue)"><span class="brand-dot"></span>Vro Klinieken</div>
<div class="abs" style="left:365px;top:3405px;width:1px;height:180px;background:#444"></div>
<span class="social" style="left:111px;background:var(--blue)"></span>
<span class="social" style="left:154px"></span>
<span class="social" style="left:197px"></span>
<span class="social" style="left:240px"></span>

<h4 class="f-head" style="left:420px;top:3403px">Snelle koppelingen</h4>
<ul class="f-list" style="left:420px;top:3442px">
  <li>» Thuis</li><li>» Behandelingen</li><li>» Over ons</li><li>» Diensten</li><li>» Bloggen</li><li>» Contact</li>
</ul>
<h4 class="f-head" style="left:629px;top:3403px">Onze koppelingen</h4>
<ul class="f-list" style="left:629px;top:3442px">
  <li>» algemene voorwaarden</li><li>» Privacybeleid</li><li>» Over ons</li><li>» Steun</li>
</ul>
<h4 class="f-head" style="left:854px;top:3403px">Contact</h4>
<div class="f-contact" style="left:854px;top:3444px;display:flex;gap:10px"><svg width="13" height="18" viewBox="0 0 13 18"><path d="M6.5 0 C10 0 13 3 13 6.5 C13 11 6.5 18 6.5 18 C6.5 18 0 11 0 6.5 C0 3 3 0 6.5 0Z" fill="#fff"/><circle cx="6.5" cy="6.5" r="2.5" fill="var(--dark)"/></svg><span>Lorem ipsum dolor sit<br>amet, consectetur adipiscing</span></div>
<div class="f-contact" style="left:854px;top:3513px;display:flex;gap:10px;align-items:center"><svg width="15" height="15" viewBox="0 0 15 15"><path d="M3 0 L6 4 L4 6 C5 9 6 10 9 11 L11 9 L15 12 L13 15 C6 15 0 9 0 2Z" fill="#fff"/></svg>+31 (079) 555 0142</div>
<div class="f-contact" style="left:854px;top:3554px;display:flex;gap:10px;align-items:center"><svg width="16" height="12" viewBox="0 0 16 12"><rect width="16" height="12" fill="#fff"/><path d="M0 0 L8 7 L16 0" stroke="var(--dark)" stroke-width="1.5" fill="none"/></svg>info@vroklinieken.nl</div>

<div class="abs" style="left:112px;top:3622px;width:976px;height:1px;background:#3a3a3c"></div>
<p class="copyright">©Copyright 2023 Vro Klinieken Zoetermeer | Alle rechten voorbehouden</p>

</body>
</html>
```